Wedding filmmaker needs artistic business card design - larkhavenmedia.ca

We are high end wedding filmmakers in a major market who produce cinematic wedding films. We require a business card design that communicates our quality, artistry, and professionalism yet looks progressive and friendly. Colors and design should skew appeal more to the bride-to-be who is usually the decision maker but not be overtly feminine per se. This means generally light pastel shades of ivory, purple, pink, yellow, as examples.
We already have a name logo established: the words "Larkhaven Media" in the font Great Vibes. Designs must use Kraft natural cardstock as the print stock and am leaning heavily toward our name logo in white, but I am open to black as well. Please design any color elements with spot white underneath where possible.
Do not try to compliment or take inspiration from our website design. Treat the card design as a separate stand alone.
Thank you so much for your hard work!

Target Market(s)

Affluent couples spending $50,000+ on their wedding

Industry/Entity Type

Progressive

Contact Information for Business Card

Peter Aldcroft
Producer
905-482-7193
www.larkhavenmedia.ca
peter@larkhavenmedia.ca
twitter @larkhaven782

Font styles to use
Serif
Sans Serif

Requirements
Must have
• - Larkhaven Media name logo (reference GIF uploaded for reference only) and catch phrase: Breathtaking wedding films (I'm open to capitalizing all three words, or just first, or all in small caps). I favor logo, and catch phrase on front of card and my contact details on the other side but if you feel strongly about a different design, go for it!
• - Design must be submitted shown on Kraft natural cardstock NOT WHITE cardstock, If you're not familiar with Kraft, this is what it looks like: http://www.quillandthreadnotes.com/wp-content/uploads/2013/07/il_570xN.738204615_pk4r.jpg
Nice to have
• - An original graphic element (eg. movie reel, bouquet, confetti, etc.) that compliments the name logo but is subtle and discreet, doesn't overpower or entangle it.
• -Great use of balance, composition, negative space, etc. I like clean tasteful design
Should not have
• -Lousy boring clip art.
• -Graphic elements, fonts, or color palette from our website
• -White cardstock background
• -designs you have previously submitted for other contests
• -Bold dark colors (eg. red, orange navy blue, etc.)
• -High tech futuristic designs like you'd create for a software company

```html
<!DOCTYPE html>
<html lang="en">
<head>
<meta charset="utf-8">
<title>Larkhaven Media – Business Card</title>
<link rel="stylesheet" href="https://fonts.googleapis.com/css2?family=Exo+2:wght@400;600&family=Cormorant+Garamond:ital,wght@0,500;1,500&display=swap">
<style>
  :root {
    --backdrop: #ece8e2;
    --kraft-light: #d3b488;
    --kraft-shade: #b8946a;
    --ink: #4a3826;
    --ink-soft: #6e5a44;
    --logo-white: #ffffff;
    --band-mauve: #b6a1c2;
    --swoosh-ivory: #f4ecdc;
    --band-text: #ffffff;
  }
  * { box-sizing: border-box; margin: 0; padding: 0; }
  html, body {
    width: 1200px; height: 899px; overflow: hidden;
    background: var(--backdrop);
    font-family: "Exo 2", Arial, sans-serif;
    color: var(--ink);
  }
  .sheet {
    width: 1200px; height: 899px;
    display: flex; align-items: center; justify-content: center; gap: 40px;
  }
  .card {
    position: relative;
    width: 540px; height: 310px;
    border-radius: 34px;
    overflow: hidden;
    background: radial-gradient(ellipse at 30% 30%, var(--kraft-light) 35%, var(--kraft-shade) 100%);
    box-shadow: 0 6px 18px rgba(60,40,20,0.18);
  }
  .wordmark {
    font-family: "Exo 2", Arial, sans-serif;
    font-weight: 400;
    color: var(--logo-white);
    white-space: nowrap;
  }
  .tagline {
    font-family: "Cormorant Garamond", Georgia, serif;
    font-weight: 500;
    font-variant: small-caps;
    color: var(--ink);
    white-space: nowrap;
  }
  .card-front .wordmark {
    position: absolute; left: 28px; top: 100px;
    font-size: 25px; letter-spacing: 0.5px;
  }
  .card-front .tagline {
    position: absolute; left: 29px; top: 136px;
    font-size: 15px; letter-spacing: 1px;
  }
  .divider {
    position: absolute; left: 240px; top: 100px;
    height: 58px; border-left: 1px dotted var(--ink-soft);
  }
  .contact {
    position: absolute; left: 262px; top: 44px;
  }
  .contact-name {
    font-size: 17px; font-weight: 600; letter-spacing: 1.5px;
    color: var(--ink); text-transform: uppercase;
  }
  .contact-title { font-size: 11px; color: var(--ink-soft); margin-top: 1px; }
  .contact-address { font-size: 13px; line-height: 17px; margin-top: 24px; }
  .contact-lines { list-style: none; margin-top: 14px; }
  .contact-lines li {
    display: flex; align-items: center; gap: 8px;
    font-size: 10px; line-height: 16px; color: var(--ink);
  }
  .contact-lines svg { width: 10px; height: 10px; fill: var(--ink); flex: none; }
  .band { position: absolute; left: 0; bottom: 0; width: 540px; height: 110px; }
  .band-url {
    position: absolute; left: 62px; bottom: 40px;
    font-size: 10.5px; letter-spacing: 1.6px; color: var(--band-text);
    transform: rotate(3deg); transform-origin: left center;
  }
  .card-back {
    display: flex; flex-direction: column; align-items: center; justify-content: center;
  }
  .card-back .wordmark { font-size: 36px; letter-spacing: 1px; }
  .card-back .tagline { font-size: 18px; letter-spacing: 1.5px; margin-top: 6px; }
</style>
</head>
<body>
<main class="sheet">
  <section class="card card-front" aria-label="Card front">
    <p class="wordmark">Larkhaven Media</p>
    <p class="tagline">Breathtaking Wedding Films</p>
    <span class="divider"></span>
    <div class="contact">
      <p class="contact-name">Marcus Hollins</p>
      <p class="contact-title">Managing Director</p>
      <p class="contact-address">417 9th floor, Birchwood<br>Road NTV</p>
      <ul class="contact-lines">
        <li><svg viewBox="0 0 10 10"><path d="M2 0.5 L3.6 0.5 L4.2 2.8 L3 3.6 Q4 5.8 6.4 7 L7.2 5.8 L9.5 6.4 L9.5 8 Q9.5 9.5 8 9.5 Q1 9 0.5 2 Q0.5 0.5 2 0.5 Z"/></svg>014 286 3957</li>
        <li><svg viewBox="0 0 10 10"><path d="M3 0 H7 Q8 0 8 1 V9 Q8 10 7 10 H3 Q2 10 2 9 V1 Q2 0 3 0 Z M3 1.5 V7.5 H7 V1.5 Z"/></svg>014 286 3957</li>
        <li><svg viewBox="0 0 10 10"><path d="M1 3 H9 V9 H1 Z M3 1 H7 V3 H3 Z"/></svg>014 286 3957</li>
        <li><svg viewBox="0 0 10 10"><path d="M0.5 2 H9.5 V8.5 H0.5 Z M1.2 2.6 L5 5.6 L8.8 2.6 V3.4 L5 6.4 L1.2 3.4 Z" fill-rule="evenodd"/></svg>yourname@mailhost.com</li>
        <li><svg viewBox="0 0 10 10"><path d="M5 0.5 A4.5 4.5 0 1 0 5 9.5 A4.5 4.5 0 1 0 5 0.5 Z M5 2 A3 3 0 1 1 5 8 A3 3 0 1 1 5 2 Z" fill-rule="evenodd"/><circle cx="5" cy="5" r="1.3"/></svg>www.yoursitename.com</li>
      </ul>
    </div>
    <svg class="band" viewBox="0 0 540 110" preserveAspectRatio="none" aria-hidden="true">
      <path d="M0 22 Q220 40 540 96 L540 110 L0 110 Z" fill="var(--swoosh-ivory)"/>
      <path d="M0 34 Q240 52 540 108 L540 110 L0 110 Z" fill="var(--band-mauve)"/>
      <path d="M0 80 Q260 98 540 110 L0 110 Z" fill="var(--swoosh-ivory)"/>
    </svg>
    <p class="band-url">www.yoursitename.com</p>
  </section>

  <section class="card card-back" aria-label="Card back">
    <p class="wordmark">Larkhaven Media</p>
    <p class="tagline">Breathtaking Wedding Films</p>
  </section>
</main>
</body>
</html>
```